Continuation of "Why Choose Us" animated gif banners campaign

The original project would not allow me to select any more designs, so I started this new project so you can submit your designs and I will purchase them.

Thanks!

```html
<!DOCTYPE html>
<html lang="en">
<head>
<meta charset="UTF-8">
<title>Contact Us Today – Banner Colour Set</title>
<link href="https://fonts.googleapis.com/css2?family=Poppins:wght@800&display=swap" rel="stylesheet">
<style>
  :root {
    --stage: #000000;
    --board: #444345;
    --card: #ffffff;
    --label: #ffffff;
    --portrait-light: #f1f1f1;
    --portrait-mid: #c9c9cc;
    --magenta: #e93bd6;
    --purple: #a83de9;
    --red: #ef2b3b;
    --orange: #f0692b;
    --yellow: #f2c232;
    --green: #31c83b;
    --blue: #2f7ff0;
    --indigo: #3b2fe8;
    --silver: #c2bebd;
    --brown: #6f473b;
    --black: #111111;
  }
  * { box-sizing: border-box; margin: 0; padding: 0; }
  html, body { width: 682px; height: 1200px; overflow: hidden; background: var(--stage); }
  .board {
    position: absolute; left: 109px; top: 0; width: 463px; height: 1200px;
    background: var(--board);
  }
  .banner {
    position: absolute; left: 31px; width: 384px; height: 89px;
    background: var(--card); overflow: hidden;
  }
  .banner--nudged { left: 38px; }
  .portrait {
    position: absolute; left: 0; top: 0; width: 92px; height: 89px;
    background: linear-gradient(180deg, var(--portrait-mid) 0%, var(--portrait-light) 100%);
  }
  .cta {
    position: absolute; left: 66px; top: 14px; width: 310px; height: 56px;
    border-radius: 12px; background: var(--tone);
    display: flex; align-items: center; justify-content: center;
    font-family: "Poppins", sans-serif; font-weight: 800; font-size: 25px;
    letter-spacing: -0.3px; color: var(--label); white-space: nowrap;
  }
  .cta::before {
    content: ""; position: absolute; left: -12px; top: 20px;
    border-top: 8px solid transparent; border-bottom: 8px solid transparent;
    border-right: 14px solid var(--tone);
  }
  .cta--magenta { --tone: var(--magenta); }
  .cta--purple { --tone: var(--purple); }
  .cta--red { --tone: var(--red); }
  .cta--orange { --tone: var(--orange); }
  .cta--yellow { --tone: var(--yellow); }
  .cta--green { --tone: var(--green); }
  .cta--blue { --tone: var(--blue); }
  .cta--indigo { --tone: var(--indigo); }
  .cta--silver { --tone: var(--silver); }
  .cta--brown { --tone: var(--brown); }
  .cta--black { --tone: var(--black); }
</style>
</head>
<body>
<main class="board">
  <section class="banner" style="top:27px"><div class="portrait" role="img" aria-label="Smiling man in shirt and tie pointing to the button"></div><p class="cta cta--magenta">CONTACT US TODAY!</p></section>
  <section class="banner" style="top:131px"><div class="portrait" role="img" aria-label="Smiling man in shirt and tie pointing to the button"></div><p class="cta cta--purple">CONTACT US TODAY!</p></section>
  <section class="banner" style="top:235px"><div class="portrait" role="img" aria-label="Smiling man in shirt and tie pointing to the button"></div><p class="cta cta--red">CONTACT US TODAY!</p></section>
  <section class="banner banner--nudged" style="top:340px"><div class="portrait" role="img" aria-label="Smiling man in shirt and tie pointing to the button"></div><p class="cta cta--orange">CONTACT US TODAY!</p></section>
  <section class="banner" style="top:444px"><div class="portrait" role="img" aria-label="Smiling man in shirt and tie pointing to the button"></div><p class="cta cta--yellow">CONTACT US TODAY!</p></section>
  <section class="banner" style="top:548px"><div class="portrait" role="img" aria-label="Smiling man in shirt and tie pointing to the button"></div><p class="cta cta--green">CONTACT US TODAY!</p></section>
  <section class="banner" style="top:652px"><div class="portrait" role="img" aria-label="Smiling man in shirt and tie pointing to the button"></div><p class="cta cta--blue">CONTACT US TODAY!</p></section>
  <section class="banner" style="top:756px"><div class="portrait" role="img" aria-label="Smiling man in shirt and tie pointing to the button"></div><p class="cta cta--indigo">CONTACT US TODAY!</p></section>
  <section class="banner" style="top:861px"><div class="portrait" role="img" aria-label="Smiling man in shirt and tie pointing to the button"></div><p class="cta cta--silver">CONTACT US TODAY!</p></section>
  <section class="banner" style="top:965px"><div class="portrait" role="img" aria-label="Smiling man in shirt and tie pointing to the button"></div><p class="cta cta--brown">CONTACT US TODAY!</p></section>
  <section class="banner banner--nudged" style="top:1069px"><div class="portrait" role="img" aria-label="Smiling man in shirt and tie pointing to the button"></div><p class="cta cta--black">CONTACT US TODAY!</p></section>
</main>
</body>
</html>
```